【 概要 】 小児科病棟訪問・特別支援学校訪問などの社会貢献活動「https://moku-hane.jp」に取り組んできました。 その活動の中で課題を感じる様になりました。 『この子たちの、この先の人生に寄与することはできないか』 そんなか障害を抱えるお子さんを持つ親御さんから、 「18歳までは(特別支援学校があるから)社会的な居場所があるけど、18際を過ぎた途端、急に居場所がなくなるんですよね」 と聞きました。 社会貢献活動をしたいと思っていたのに、そんな事も知らなかったのかと恥じました。 知ったからには行動しよう! そして多くの方のご意見をいただき、障害者就労継続支援B型事業所を開所することとなりました。 <参考> いくつかあるメディア掲載記事をご覧ください。 https://www.tsuzuri-news.jp/article/KQ7RTM04BX9PL2C300D1000000/ https://www.vidorama.jp/watch?v=Qx4bTnw82Lk https://tane-maku.jp/projects/view/817460 【会社名】 株式会社Kolu Step 【事業所名】 Kolu Nest さいたま 【キャッチコピー】 笑顔でつなぐ、未来への道 【 依頼内容 】 ・サイズ:A4 両面 3つ折り仕様 ・ページ数:1ページ ・素材の用意(画像・文章等):会社ロゴ・代表宣材写真・養蜂の様子は用意します。その他必要な写真があれば可能な範囲でお応えします。 ・デザイン内容:利用者さんの集客や仕事の受注につながる様なデザイン 【掲載内容】 ●表紙 ●あいさつ(概要) ●ご利用までの流れ ①問い合わせ →まずは、お電話かメールにてお問い合わせください。 ②見学 →事業所の雰囲気をご覧いただき、スタッフとお話ししてみてください。 ③体験実習 →3日から1週間程度、ご都合に合わせて通っていただきます。 ④利用開始 →利用契約を結び、正式に利用開始となります。 ●対象 65歳未満で就労の意思があり、『障害福祉サービス受給者証』をお持ちの方です。 ●利用料金 原則1割負担ですが、多くの場合は無料でご利用いただけます。受給者証の取得など、必要であればお手伝いいたします。 ●利用開始前に 見学→体験実習をおすすめします。ご自身に合うか確かめてからご利用ください。 ●作業内容 ・養蜂 →障がい者の就労機会の創出と地域交流の促進につながるプロジェクトになることが期待されます。(見沼区地域にて作業) ・コーヒー豆 →生豆の中に数パーセント含まれる、形や大きさが不揃いな豆や青カビが付着した豆を丁寧に取り除いていきます。 その後梱包・発送まで担います。 ・古本ネット販売 →回収した本の仕分け、清掃、出品、梱包、配送など、ネット通販を行います。 ●アクセス ●お問い合わせ 【 デザインイメージ 】 ・ターゲット層:障害を持つ方、またそのご家族。障害者雇用に関心のある企業の方。 ・雰囲気:親しみやすくおしゃれな雰囲気 【 契約金額(税抜) 】 3万円 ※上記記載内容をベースとし、柔軟に編集いただければと思います。(表記の仕方などはお任せします) ※契約金額(税込)からシステム利用料を差し引いた金額が、ワーカーさまの受取金額となります。 その他ご質問等ありましたら、気軽にお問い合わせください。 写真などの素材も必要であれば、お問い合わせください。 ご応募をお待ちしております! |
採用の理由
色使いやレイアウト等、事業所の理念や私(代表)の想い通りのデザインをしていただきました。
また、度重なる細かい修正依頼にもスピーディーに快く引き受けてくださいました。
応募者全員へのお礼・コメント
皆様たくさんのご提案をいただきありがとうございました。
どれも素敵なデザインで選定するのが非常に困難でした。
十分な報酬をお支払いできないにも関わらず、たくさんのご提案をいただけたこと大変感謝申し上げます。
引き続き弊社の活動を応援していただけますと幸いに存じます。

```html
<!DOCTYPE html>
<html lang="ja">
<head>
<meta charset="utf-8">
<title>Kolu Nest さいたま 三つ折りパンフレット</title>
<link rel="stylesheet" href="https://fonts.googleapis.com/css2?family=Noto+Sans+JP:wght@400;500;700;900&display=swap">
<style>
:root{
  --stage:#d9d9d9;
  --kraft:#e6dccb;
  --ink:#3a3430;
  --ink-soft:#6b625a;
  --red:#c8252c;
  --red-deep:#a81c22;
  --white:#ffffff;
}
*{box-sizing:border-box;margin:0;padding:0}
html,body{width:856px;height:1200px;overflow:hidden;background:var(--stage)}
body{font-family:"Noto Sans JP",sans-serif;color:var(--ink);position:relative}
.spread{position:absolute;left:28px;width:800px;height:560px;background:var(--kraft);display:grid;grid-template-columns:repeat(3,1fr);box-shadow:0 2px 6px rgba(0,0,0,.18)}
.spread--outer{top:22px}
.spread--inner{top:612px;grid-template-columns:2fr 1fr}
.panel{position:relative;padding:22px 20px;border-right:1px dashed rgba(0,0,0,.08);overflow:hidden}
.panel:last-child{border-right:none}

/* cover */
.cover__sub{font-size:12px;font-weight:700;margin-top:70px}
.cover__title{font-size:21px;font-weight:900;letter-spacing:.01em;margin-top:4px;white-space:nowrap}
.cover__tag{display:inline-block;margin-top:12px;background:var(--red);color:var(--white);font-size:11px;font-weight:700;padding:4px 14px}
.cover__art{margin-top:22px;height:200px;border-radius:4px;background:linear-gradient(160deg,#efe7da,#d9cdb8)}
.cover__brand{position:absolute;left:20px;bottom:48px;display:flex;align-items:center;gap:6px;font-size:16px;font-weight:700}
.cover__brand i{width:10px;height:10px;border-radius:50%;background:var(--red)}
.cover__copy{position:absolute;left:20px;bottom:26px;font-size:10px;color:var(--ink-soft)}

/* access */
.map{height:148px;background:linear-gradient(135deg,#f3ede2,#e2d7c3);border-radius:3px;margin:18px 0 10px}
.site{margin-bottom:10px}
.site__head{display:flex;align-items:center;gap:6px;font-size:12px;font-weight:700}
.num{width:16px;height:16px;border-radius:50%;background:var(--red);color:var(--white);font-size:10px;display:grid;place-items:center}
.site__addr{font-size:8.5px;color:var(--ink-soft);margin:3px 0 0 22px}
.company{position:absolute;left:20px;right:20px;bottom:30px}
.company__name{font-size:18px;font-weight:700;margin-bottom:6px}
.contact{display:flex;align-items:center;gap:6px;font-size:9px;margin-top:4px}
.contact--tel{font-size:19px;font-weight:700;letter-spacing:.02em}
.contact svg{flex:none}

/* greeting */
.portrait{height:150px;background:linear-gradient(180deg,#cfcfcf,#8e8e8e);border-radius:2px}
.greet__org{font-size:10px;text-align:right;margin-top:10px}
.greet__name{font-size:9px;text-align:right}
.greet__name b{font-size:13px;margin-left:6px}
.greet__text{font-size:8.6px;line-height:1.75;margin-top:12px}

/* work */
.work{padding:18px 20px}
.work__band{background:var(--red);color:var(--white);text-align:center;font-size:12px;font-weight:700;padding:4px 0;margin:0 -20px 12px}
.work__grid{display:grid;grid-template-columns:1fr 1fr;gap:10px}
.photo{border-radius:2px}
.photo--bees{height:140px;background:linear-gradient(140deg,#b98a3a,#6e4b1f)}
.photo--forest{height:140px;background:linear-gradient(160deg,#7f9b63,#3f5a33)}
.photo--beans{height:120px;background:linear-gradient(150deg,#6e4426,#3b2314)}
.photo--books{height:120px;background:linear-gradient(150deg,#b08a63,#6a4c33)}
.item__title{font-size:15px;font-weight:900;color:var(--red);margin-top:6px}
.item__text{font-size:8.5px;line-height:1.6;margin-top:2px}

/* guide */
.guide{background:linear-gradient(180deg,var(--red),var(--red-deep));color:var(--white);padding:18px}
.guide__head{background:var(--white);color:var(--red);font-weight:700;font-size:12px;text-align:center;padding:4px 0;margin-bottom:10px}
.guide__block{font-size:8.5px;line-height:1.55;margin-bottom:8px}
.guide__block b{display:block;font-size:10px}
.step{display:flex;gap:8px;margin-bottom:6px;align-items:flex-start}
.step__label{font-size:11px;font-weight:700;white-space:nowrap}
.step__body{font-size:8.5px;line-height:1.5}
.step__box{background:var(--white);color:var(--ink);padding:4px 8px;border-radius:2px;margin-top:3px}
.step__box .tel{font-size:15px;font-weight:700;color:var(--red)}
.step__box .mail{font-size:10px;font-weight:700}
</style>
</head>
<body>

<section class="spread spread--outer">
  <article class="panel cover">
    <p class="cover__sub">障害者就労継続支援B型事業所</p>
    <h1 class="cover__title">Kolu Nest さいたま</h1>
    <span class="cover__tag">新規OPEN</span>
    <div class="cover__art" role="img" aria-label="握手を交わす二人の線画イラスト"></div>
    <p class="cover__brand"><i></i>Kolu Step</p>
    <p class="cover__copy">笑顔でつなぐ、未来への道</p>
  </article>

  <article class="panel access">
    <div class="site">
      <p class="site__head"><span class="num">1</span>養蜂場</p>
      <p class="site__addr">埼玉県さいたま市見沼区みどり町0-0-0</p>
    </div>
    <div class="map" role="img" aria-label="事業所周辺の案内地図"></div>
    <div class="site">
      <p class="site__head"><span class="num">2</span>その他の作業場所</p>
      <p class="site__addr">埼玉県さいたま市北区あおば町0-0-0</p>
    </div>
    <div class="company">
      <p class="company__name">株式会社Kolu Step</p>
      <p class="contact"><svg width="10" height="12" viewBox="0 0 10 12"><path d="M5 0a4 4 0 0 0-4 4c0 3 4 8 4 8s4-5 4-8a4 4 0 0 0-4-4zm0 5.5A1.5 1.5 0 1 1 5 2.5a1.5 1.5 0 0 1 0 3z" fill="#c8252c"/></svg>埼玉県さいたま市北区あおば町0-0-0</p>
      <p class="contact contact--tel"><svg width="14" height="14" viewBox="0 0 14 14"><path d="M3 1l2 3-1.2 1.2a8 8 0 0 0 5 5L10 9l3 2-1 2.5C6 13 1 8 .5 2z" fill="#3a3430"/></svg>012-987-65432</p>
      <p class="contact"><svg width="12" height="9" viewBox="0 0 12 9"><rect x=".5" y=".5" width="11" height="8" fill="none" stroke="#3a3430"/><path d="M.5.5l5.5 4 5.5-4" fill="none" stroke="#3a3430"/></svg>kolustep@mail.co.jp</p>
      <p class="contact"><svg width="11" height="11" viewBox="0 0 11 11"><circle cx="5.5" cy="5.5" r="5" fill="none" stroke="#3a3430"/><path d="M.5 5.5h10M5.5.5c3 3 3 7 0 10M5.5.5c-3 3-3 7 0 10" fill="none" stroke="#3a3430" stroke-width=".8"/></svg>https://moku-hane.jp</p>
    </div>
  </article>

  <article class="panel greet">
    <div class="portrait" role="img" aria-label="代表取締役の宣材写真"></div>
    <p class="greet__org">株式会社Kolu Step</p>
    <p class="greet__name">代表取締役<b>相馬 大翔</b></p>
    <p class="greet__text">これまで小児科病棟訪問や特別支援学校訪問などの社会貢献活動に取り組んできました。その中で「この子たちの、この先の人生に寄与できないか」と考えるようになりました。<br>「18歳までは居場所があるけど、18歳を過ぎた途端、急に居場所がなくなる」──親御さんのその言葉に、知らなかった自分を恥じました。<br>知ったからには行動しよう。多くの方のご意見をいただき、障害者就労継続支援B型事業所を開所いたしました。一人ひとりが笑顔で働ける場所を、地域の皆さまと一緒につくってまいります。</p>
  </article>
</section>

<section class="spread spread--inner">
  <article class="panel work">
    <h2 class="work__band">作業内容</h2>
    <div class="work__grid">
      <div>
        <div class="photo photo--bees" role="img" aria-label="巣箱の枠にびっしりと付いたミツバチの写真"></div>
        <p class="item__title">養蜂</p>
        <p class="item__text">障がい者の就労機会の創出と地域交流の促進につながるプロジェクトになることが期待されます。（見沼区地域にて作業）</p>
      </div>
      <div class="photo photo--forest" role="img" aria-label="養蜂場のある竹林と木立の写真"></div>
      <div>
        <div class="photo photo--beans" role="img" aria-label="コーヒー生豆の写真"></div>
        <p class="item__title">コーヒー豆</p>
        <p class="item__text">生豆の中に数パーセント含まれる、形や大きさが不揃いな豆や青カビが付着した豆を丁寧に取り除きます。その後梱包・発送まで担います。</p>
      </div>
      <div>
        <div class="photo photo--books" role="img" aria-label="積み重ねられた古本の写真"></div>
        <p class="item__title">古本販売</p>
        <p class="item__text">回収した本の仕分け、清掃、出品、梱包、配送など、ネット通販を行います。</p>
      </div>
    </div>
  </article>

  <article class="panel guide">
    <h2 class="guide__head">ご利用に際して</h2>
    <div class="guide__block"><b>■ 対象</b>65歳未満で就労の意思があり、『障害福祉サービス受給者証』をお持ちの方です。</div>
    <div class="guide__block"><b>■ 利用料金</b>原則1割負担ですが、多くの場合は無料でご利用いただけます。受給者証の取得など、必要であればお手伝いいたします。</div>
    <div class="guide__block"><b>■ ご利用開始前に</b>見学→体験実習をおすすめします。ご自身に合うか確かめてからご利用ください。</div>
    <h2 class="guide__head">ご利用開始までの流れ</h2>
    <div class="step"><span class="step__label">STEP 1</span>
      <div class="step__body">お問い合わせ<br>まずは、お電話かメールにてお問い合わせください。
        <div class="step__box"><span class="tel">012-987-65432</span><br><span class="mail">kolustep@mail.co.jp</span></div>
      </div>
    </div>
    <div class="step"><span class="step__label">STEP 2</span><div class="step__body">見学<br>事業所の雰囲気をご覧いただき、スタッフとお話ししてみてください。</div></div>
    <div class="step"><span class="step__label">STEP 3</span><div class="step__body">体験実習<br>3日から1週間程度、ご都合に合わせて通っていただきます。</div></div>
    <div class="step"><span class="step__label">STEP 4</span><div class="step__body">利用開始<br>利用契約を結び、正式に利用開始となります。</div></div>
  </article>
</section>

</body>
</html>
```